Dental office Stationary & Business card
Marlowe Pines Dental LLC
Dental office Stationary & Business card - Health
Creative Brief
Professional
Implants- Cosmetics- Generals- Braces
2815 Quarry Hollow Pkwy. Unit 3407 Norcross, GA 30071
mpdoffice@tinmail.example
www.marlowepinesdental.example
We would like designers to include for us the following: business card, letter head, envelope label, and e-signature template. logo design files can be downloaded below: https://www.filecrate.example/s/q8zrt3mw1xk5pa/Modern%20logo%20for%20a%20dental%20office.zip
Please have this content in the back of the card. "Your next appointment is on ____________ at _______ AM/PM

```html
<!DOCTYPE html>
<html lang="en">
<head>
<meta charset="utf-8">
<title>Marlowe Pines Dental – Business Card</title>
<link href="https://fonts.googleapis.com/css2?family=Open+Sans:wght@400;600;700&display=swap" rel="stylesheet">
<style>
  :root {
    --backdrop: #e6e4e1;
    --card: #ffffff;
    --brown: #6b3a22;
    --tan: #c9a27a;
    --ink: #343434;
    --ink-soft: #4a4a4a;
  }
  html, body {
    margin: 0;
    padding: 0;
    width: 1200px;
    height: 816px;
    overflow: hidden;
    background: var(--backdrop);
    font-family: "Open Sans", Arial, sans-serif;
  }
  .business-card {
    position: absolute;
    left: 75px;
    top: 108px;
    width: 1050px;
    height: 600px;
    background: var(--card);
    border-radius: 34px;
    overflow: hidden;
    box-shadow: 0 6px 22px rgba(0,0,0,0.18);
  }
  .card-band {
    position: absolute;
    left: 0;
    top: 0;
    width: 1050px;
    height: 600px;
  }
  .brand {
    position: absolute;
    left: 640px;
    top: 175px;
    width: 330px;
    display: flex;
    align-items: center;
    justify-content: flex-end;
    gap: 16px;
  }
  .brand-dot {
    width: 26px;
    height: 26px;
    border-radius: 50%;
    background: var(--brown);
    flex: none;
  }
  .brand-name {
    color: var(--brown);
    font-weight: 600;
    font-size: 34px;
    line-height: 1.1;
    text-align: right;
  }
  .holder {
    position: absolute;
    left: 70px;
    top: 215px;
  }
  .holder-name {
    margin: 0;
    color: var(--ink);
    font-weight: 700;
    font-size: 38px;
    letter-spacing: 0.5px;
  }
  .holder-title {
    margin: 4px 0 0;
    color: var(--brown);
    font-weight: 400;
    font-size: 28px;
  }
  .contact-list {
    position: absolute;
    left: 70px;
    top: 345px;
    margin: 0;
    padding: 0;
    list-style: none;
    color: var(--ink-soft);
    font-size: 21px;
    font-weight: 600;
    line-height: 1.3;
  }
  .contact-list li {
    display: flex;
    align-items: flex-start;
    gap: 14px;
    margin-bottom: 4px;
  }
  .contact-list svg {
    width: 20px;
    height: 20px;
    flex: none;
    margin-top: 4px;
    fill: var(--brown);
  }
  .address { max-width: 300px; }
  .web-pill {
    position: absolute;
    left: 620px;
    top: 440px;
    width: 420px;
    height: 56px;
    box-sizing: border-box;
    padding: 0 26px;
    display: flex;
    align-items: center;
    justify-content: center;
    color: #ffffff;
    font-size: 20px;
    font-weight: 600;
    white-space: nowrap;
  }
</style>
</head>
<body>
  <div class="business-card">
    <svg class="card-band" viewBox="0 0 1050 600" aria-hidden="true">
      <path d="M0 520 L555 520 Q580 520 592 500 L610 470 Q620 455 640 452 L1050 452 L1050 600 L0 600 Z" fill="var(--brown)"/>
      <rect x="620" y="432" width="420" height="72" rx="36" fill="var(--brown)" stroke="var(--tan)" stroke-width="5"/>
    </svg>

    <div class="brand">
      <span class="brand-dot"></span>
      <span class="brand-name">Marlowe Pines<br>Dental</span>
    </div>

    <div class="holder">
      <h1 class="holder-name">JORDAN ELLERY</h1>
      <p class="holder-title">Managing Director</p>
    </div>

    <ul class="contact-list">
      <li>
        <svg viewBox="0 0 24 24"><path d="M12 2a7 7 0 0 0-7 7c0 5 7 13 7 13s7-8 7-13a7 7 0 0 0-7-7zm0 9.5a2.5 2.5 0 1 1 0-5 2.5 2.5 0 0 1 0 5z"/></svg>
        <span class="address">2815 Quarry Hollow Pkwy. Unit 3407</span>
      </li>
      <li>
        <svg viewBox="0 0 24 24"><path d="M6.6 10.8a15 15 0 0 0 6.6 6.6l2.2-2.2a1 1 0 0 1 1-.25 11.4 11.4 0 0 0 3.6.6 1 1 0 0 1 1 1V20a1 1 0 0 1-1 1A17 17 0 0 1 3 4a1 1 0 0 1 1-1h3.5a1 1 0 0 1 1 1c0 1.25.2 2.45.6 3.6a1 1 0 0 1-.25 1z"/></svg>
        <span>012 555 0147</span>
      </li>
      <li>
        <svg viewBox="0 0 24 24"><path d="M6.6 10.8a15 15 0 0 0 6.6 6.6l2.2-2.2a1 1 0 0 1 1-.25 11.4 11.4 0 0 0 3.6.6 1 1 0 0 1 1 1V20a1 1 0 0 1-1 1A17 17 0 0 1 3 4a1 1 0 0 1 1-1h3.5a1 1 0 0 1 1 1c0 1.25.2 2.45.6 3.6a1 1 0 0 1-.25 1z"/></svg>
        <span>012 555 0147</span>
      </li>
      <li>
        <svg viewBox="0 0 24 24"><path d="M3 5h18v14H3z M3 5l9 7 9-7" fill="none" stroke="var(--brown)" stroke-width="2.2"/></svg>
        <span>mpdoffice@tinmail.example</span>
      </li>
    </ul>

    <div class="web-pill">www.marlowepinesdental.example</div>
  </div>
</body>
</html>
```